STI/STD Medical Clinic- Wellspring Crest Partners, Inc Website

We are a STI clinic in florida looking for a website. We want to be professional but also playful. We want a buildout similar to the website listed below as our clinic is very similar to theirs.

This is a great example of a clinic doing similar stuff as us. We obviously do not want their color scheme but their format and buildout work. Please see our logo attached for color schemes etc.

https://bluefernclinicmiami.org

Industry/Entity Type

Medical

Coding

Coded - Design and coding required

Number of Pages Required

5+ page

Font styles to use
Sans Serif

```html
<!DOCTYPE html>
<html lang="en">
<head>
<meta charset="utf-8">
<title>Wellspring Crest Partners, Inc</title>
<link href="https://fonts.googleapis.com/css2?family=Josefin+Sans:wght@400;600;700&family=Montserrat:wght@400;500;600;700&display=swap" rel="stylesheet">
<style>
:root{
  --navy:#1c3b8b;
  --navy-deep:#152c6b;
  --ink:#1d2330;
  --text:#3b4150;
  --muted:#7b8190;
  --blue:#0e7ef0;
  --violet:#4a3df0;
  --pink:#f2507e;
  --grad:linear-gradient(90deg,var(--violet),var(--pink));
  --white:#ffffff;
  --field:#ffffff;
  --card-shadow:0 10px 26px rgba(20,30,70,.14);
}
*{box-sizing:border-box;margin:0;padding:0}
html,body{width:1200px;height:4330px;overflow:hidden}
body{position:relative;background:var(--white);font-family:"Montserrat",sans-serif;color:var(--text)}
.abs{position:absolute}
.heading{font-family:"Josefin Sans",sans-serif;color:var(--ink)}
.eyebrow{font-family:"Montserrat",sans-serif;font-size:13px;font-weight:500;letter-spacing:.6px;text-transform:uppercase;color:var(--ink)}
.btn{position:absolute;display:flex;align-items:center;justify-content:center;border-radius:30px;background:var(--grad);color:#fff;font-family:"Josefin Sans",sans-serif;font-weight:700;font-size:17px;letter-spacing:.5px;box-shadow:0 8px 20px rgba(74,61,240,.25)}
.para{font-size:14px;line-height:22px}

/* header */
.site-header{position:absolute;left:0;top:0;width:1200px;height:83px;background:#fff;border-top:3px solid var(--violet)}
.brand{position:absolute;display:flex;align-items:center;gap:10px}
.brand-dot{width:38px;height:38px;border-radius:50%;background:var(--grad)}
.brand-name{font-family:"Josefin Sans",sans-serif;font-weight:700;font-size:22px;color:var(--navy);line-height:1}
.nav{position:absolute;top:35px;font-size:14px;color:var(--ink)}
.portal{position:absolute;left:888px;top:22px;width:190px;height:44px;border:2px solid var(--pink);border-radius:24px;display:flex;align-items:center;justify-content:center;gap:8px;color:var(--violet);font-family:"Josefin Sans",sans-serif;font-weight:700;font-size:17px}

/* hero */
.hero-photo{position:absolute;left:0;top:83px;width:1200px;height:590px;background:linear-gradient(180deg,#d98a3e 0%,#c0753c 25%,#7c5137 55%,#3e2a22 100%)}
.hero-title-small{left:122px;top:210px;color:#fff;font-family:"Josefin Sans",sans-serif;font-weight:600;font-size:22px;letter-spacing:1.5px}
.hero-title{left:120px;top:238px;color:#fff;font-family:"Josefin Sans",sans-serif;font-weight:600;font-size:58px;letter-spacing:2px}
.hero-text{left:122px;top:318px;width:445px;color:#fff}

/* about */
.about-back{left:138px;top:738px;width:440px;height:412px;border-radius:46px;background:var(--grad);transform:rotate(-4deg)}
.about-photo{left:160px;top:775px;width:405px;height:365px;border-radius:40px;background:linear-gradient(160deg,#f1f3f6,#dfe3ea 55%,#c9ced8);box-shadow:var(--card-shadow)}

/* services */
.card{position:absolute;width:220px;height:258px;background:#fff;clip-path:polygon(0 8%,100% 0,100% 92%,0 100%);box-shadow:var(--card-shadow);text-align:center;padding:40px 24px 0}
.card.alt{clip-path:polygon(0 0,100% 8%,100% 100%,0 92%)}
.card svg.icon{width:52px;height:52px}
.card h3{font-family:"Josefin Sans",sans-serif;font-size:15px;font-weight:700;color:var(--ink);margin:10px 0 12px;letter-spacing:.6px;line-height:18px}
.card p{font-size:10.5px;line-height:17px;color:var(--text)}
.card .arrow{position:absolute;left:96px;bottom:34px}

/* team */
.team-photo{position:absolute;width:278px;height:330px;background:linear-gradient(160deg,#eef1f4,#cfd7df 60%,#b7c1cc);clip-path:polygon(0 4%,100% 0,100% 100%,0 100%)}
.team-card{position:absolute;width:270px;height:180px;background:#f1f1f3;clip-path:polygon(0 6%,100% 0,100% 100%,0 96%);box-shadow:var(--card-shadow);text-align:center;padding-top:42px}
.team-card h4{font-family:"Josefin Sans",sans-serif;font-size:18px;font-weight:600;color:var(--ink)}
.team-card .role{font-size:12px;color:var(--blue);margin:4px 0 10px}
.team-card p{font-size:10.5px;line-height:17px;padding:0 26px}
.nav-circle{position:absolute;width:64px;height:64px;border-radius:50%;display:flex;align-items:center;justify-content:center}

/* contact */
.field{position:absolute;background:var(--field);border-radius:22px;font-size:14px;color:var(--muted);padding:0 26px;display:flex;align-items:center}

/* footer */
.foot-title{font-size:19px;color:var(--ink)}
.foot-link{font-size:14px;color:var(--ink)}
.social{position:absolute;width:26px;height:26px;border-radius:50%;background:var(--blue)}
.bottom-bar{left:0;top:4298px;width:1200px;height:32px;background:var(--navy-deep);color:#fff;font-size:10.5px}
</style>
</head>
<body>

<!-- Header -->
<header class="site-header">
  <div class="brand" style="left:126px;top:18px"><span class="brand-dot"></span><span class="brand-name">Wellspring Crest</span></div>
  <span class="nav" style="left:432px">Home</span>
  <span class="nav" style="left:505px">About</span>
  <span class="nav" style="left:578px">Meet The Team</span>
  <span class="nav" style="left:713px">Services</span>
  <span class="nav" style="left:800px">Contact</span>
  <div class="portal">
    <svg width="14" height="14" viewBox="0 0 14 14"><circle cx="7" cy="4" r="3" fill="var(--violet)"/><path d="M1 13c0-3.5 2.7-5 6-5s6 1.5 6 5z" fill="var(--violet)"/></svg>
    Patient Portal
  </div>
</header>

<!-- Hero -->
<div class="hero-photo" role="img" aria-label="Couple walking hand in hand along a beach at sunset"></div>
<div class="abs hero-title-small">WELLSPRING</div>
<div class="abs hero-title">CREST PARTNERS</div>
<p class="abs hero-text para">Lorem ipsum dolor sit amet, consectetur adipiscing elit. Id blandit sed mattis amet scelerisque in risus in. Magna tincidunt sit arcu viverra massa egestas velit sapien.</p>
<div class="btn" style="left:122px;top:422px;width:270px;height:52px">Make An Appointment</div>
<svg class="abs" style="left:0;top:590px" width="1200" height="100" viewBox="0 0 1200 100">
  <defs><linearGradient id="wg" x1="0" x2="1"><stop offset="0" stop-color="#4a3df0"/><stop offset="1" stop-color="#f2507e"/></linearGradient></defs>
  <path d="M0 58C180 20 380 10 620 48S1000 80 1200 28V100H0Z" fill="url(#wg)"/>
  <path d="M0 70C200 34 390 30 620 62S1000 92 1200 46V100H0Z" fill="#fff"/>
</svg>

<!-- About -->
<div class="abs about-back"></div>
<div class="abs about-photo" role="img" aria-label="Smiling doctor in a white coat seated at a desk"></div>
<div class="abs eyebrow" style="left:670px;top:814px">Welcome to Wellspring Crest</div>
<h2 class="abs heading" style="left:670px;top:836px;font-size:40px;font-weight:400;letter-spacing:1px">About Us</h2>
<p class="abs para" style="left:670px;top:896px;width:410px">Lorem ipsum dolor sit amet, consectetur adipiscing elit. Id blandit sed mattis amet scelerisque in risus in. Magna tincidunt sit arcu viverra massa egestas velit sapien. Convallis ipsum velit vitae massa felis quis. Eget odio dignissim pellentesque et mi diam ut.</p>
<div class="btn" style="left:670px;top:1043px;width:165px;height:52px">Reed More</div>

<!-- Services -->
<svg class="abs" style="left:0;top:1215px" width="1200" height="930" viewBox="0 0 1200 930">
  <path d="M0 60C260 50 520 -20 800 10S1100 40 1200 40V870C1000 870 780 910 520 880S120 860 0 880Z" fill="var(--navy)"/>
</svg>
<div class="abs eyebrow" style="left:0;top:1356px;width:1200px;text-align:center;color:#fff">What we do</div>
<h2 class="abs heading" style="left:0;top:1376px;width:1200px;text-align:center;font-size:42px;font-weight:400;color:#fff;letter-spacing:1px">Services We Prowide</h2>

<svg width="0" height="0" style="position:absolute"><defs><linearGradient id="ig" x1="0" x2="1" y1="0" y2="1"><stop offset="0" stop-color="#4a3df0"/><stop offset="1" stop-color="#f2507e"/></linearGradient></defs></svg>

<div class="card" style="left:122px;top:1452px">
  <svg class="icon" viewBox="0 0 52 52" fill="none" stroke="url(#ig)" stroke-width="2.5"><path d="M12 6v14a8 8 0 0016 0V6"/><path d="M20 28v8a8 8 0 0016 0v-6"/><circle cx="36" cy="26" r="4"/></svg>
  <h3>PrEP</h3><p>Lorem ipsum dolor sit amet, consectetur adipiscing elit. Id blandit sed mattis amet.</p>
  <svg class="arrow" width="26" height="10" viewBox="0 0 26 10" fill="none" stroke="var(--pink)" stroke-width="1.5"><path d="M0 5h24M19 1l5 4-5 4"/></svg>
</div>
<div class="card alt" style="left:367px;top:1452px">
  <svg class="icon" viewBox="0 0 52 52" fill="none" stroke="url(#ig)" stroke-width="2.5"><rect x="8" y="10" width="22" height="14" rx="7" transform="rotate(-40 19 17)"/><ellipse cx="32" cy="34" rx="12" ry="8"/></svg>
  <h3>PEP</h3><p>Lorem ipsum dolor sit amet, consectetur adipiscing elit. Id blandit sed mattis amet.</p>
  <svg class="arrow" width="26" height="10" viewBox="0 0 26 10" fill="none" stroke="var(--pink)" stroke-width="1.5"><path d="M0 5h24M19 1l5 4-5 4"/></svg>
</div>
<div class="card" style="left:612px;top:1452px">
  <svg class="icon" viewBox="0 0 52 52" fill="none" stroke="url(#ig)" stroke-width="2.5"><path d="M6 14c12-6 30-6 40 0-2 14-10 24-22 26-8-4-16-14-18-26z"/><path d="M26 16v20"/></svg>
  <h3>HEPATITIS C</h3><p>Lorem ipsum dolor sit amet, consectetur adipiscing elit. Id blandit sed mattis amet.</p>
  <svg class="arrow" width="26" height="10" viewBox="0 0 26 10" fill="none" stroke="var(--pink)" stroke-width="1.5"><path d="M0 5h24M19 1l5 4-5 4"/></svg>
</div>
<div class="card alt" style="left:857px;top:1452px">
  <svg class="icon" viewBox="0 0 52 52" fill="none" stroke="url(#ig)" stroke-width="2.5"><path d="M26 6c-6 0-8 8-4 14l14 22M26 6c6 0 8 8 4 14L16 42"/></svg>
  <h3>HIV</h3><p>Lorem ipsum dolor sit amet, consectetur adipiscing elit. Id blandit sed mattis amet.</p>
  <svg class="arrow" width="26" height="10" viewBox="0 0 26 10" fill="none" stroke="var(--pink)" stroke-width="1.5"><path d="M0 5h24M19 1l5 4-5 4"/></svg>
</div>

<div class="card alt" style="left:122px;top:1716px">
  <svg class="icon" viewBox="0 0 52 52" fill="none" stroke="url(#ig)" stroke-width="2.5"><rect x="8" y="8" width="36" height="36" rx="4"/><circle cx="26" cy="26" r="10"/><circle cx="26" cy="26" r="5"/></svg>
  <h3>STI</h3><p>Lorem ipsum dolor sit amet, consectetur adipiscing elit. Id blandit sed mattis amet.</p>
  <svg class="arrow" width="26" height="10" viewBox="0 0 26 10" fill="none" stroke="var(--pink)" stroke-width="1.5"><path d="M0 5h24M19 1l5 4-5 4"/></svg>
</div>
<div class="card" style="left:367px;top:1716px">
  <svg class="icon" viewBox="0 0 52 52" fill="none" stroke="url(#ig)" stroke-width="2.5"><rect x="8" y="8" width="30" height="38" rx="3"/><path d="M14 18h18M14 26h18M14 34h10M42 14l-12 22"/></svg>
  <h3>CASE MANAGEMENT</h3><p>Lorem ipsum dolor sit amet, consectetur adipiscing elit. Id blandit sed mattis amet.</p>
  <svg class="arrow" width="26" height="10" viewBox="0 0 26 10" fill="none" stroke="var(--pink)" stroke-width="1.5"><path d="M0 5h24M19 1l5 4-5 4"/></svg>
</div>
<div class="card alt" style="left:612px;top:1716px">
  <svg class="icon" viewBox="0 0 52 52" fill="none" stroke="url(#ig)" stroke-width="2.5"><rect x="12" y="10" width="20" height="36" rx="3"/><rect x="26" y="6" width="18" height="14" rx="2"/><circle cx="22" cy="32" r="4"/></svg>
  <h3>TELEHEALTH</h3><p>Lorem ipsum dolor sit amet, consectetur adipiscing elit. Id blandit sed mattis amet.</p>
  <svg class="arrow" width="26" height="10" viewBox="0 0 26 10" fill="none" stroke="var(--pink)" stroke-width="1.5"><path d="M0 5h24M19 1l5 4-5 4"/></svg>
</div>
<div class="card" style="left:857px;top:1716px;padding-top:32px">
  <svg class="icon" viewBox="0 0 52 52" fill="none" stroke="url(#ig)" stroke-width="2.5"><path d="M6 8h26v16H16l-6 6v-6H6z"/><path d="M22 24v6h16l6 6v-6h2V16h-8"/></svg>
  <h3 style="margin-top:4px">LANGUAGE INTERPRETATION SERVICES</h3><p>Lorem ipsum dolor sit amet, consectetur adipiscing elit.</p>
  <svg class="arrow" width="26" height="10" viewBox="0 0 26 10" fill="none" stroke="var(--pink)" stroke-width="1.5"><path d="M0 5h24M19 1l5 4-5 4"/></svg>
</div>

<!-- Visit -->
<div class="abs eyebrow" style="left:122px;top:2284px">Make an appointment</div>
<h2 class="abs heading" style="left:122px;top:2308px;font-size:40px;font-weight:400;letter-spacing:1.5px">VISIT US TODAY</h2>
<p class="abs para" style="left:122px;top:2380px;width:390px">Lorem ipsum dolor sit amet, consectetur adipiscing elit. Id blandit sed mattis amet scelerisque in risus in. Magna tincidunt sit arcu viverra massa egestas velit sapien. Convallis ipsum velit vitae massa felis quis. Eget odio dignissim pellentesque et mi diam ut.</p>
<div class="btn" style="left:122px;top:2530px;width:270px;height:52px">Make An Appointment</div>
<div class="abs" style="left:700px;top:2224px;width:380px;height:296px;background:var(--blue);border-radius:120px 0 0 0;clip-path:polygon(0 0,100% 0,100% 100%,0 100%)"></div>
<div class="abs" style="left:570px;top:2245px;width:490px;height:400px;border-radius:60px;background:linear-gradient(150deg,#e8e3dc,#c9b6a2 50%,#8f7a6b);" role="img" aria-label="Smiling couple seated together at a clinic consultation"></div>

<!-- Team -->
<div class="abs eyebrow" style="left:0;top:2770px;width:1200px;text-align:center">Stuff</div>
<h2 class="abs heading" style="left:0;top:2792px;width:1200px;text-align:center;font-size:42px;font-weight:400;letter-spacing:2px">OUR TEAM</h2>

<div class="team-photo" style="left:122px;top:2870px" role="img" aria-label="Portrait of a male doctor with a stethoscope"></div>
<div class="team-card" style="left:155px;top:3080px"><h4>Dr. Marcus Bell</h4><div class="role">Lorem ipsum</div><p>Lorem ipsum dolor sit amet, consectetur adipiscing elit. Id blandit sed mattis amet scelerisque in risus in.</p></div>

<div class="team-photo" style="left:449px;top:2870px" role="img" aria-label="Portrait of a female doctor in a lab coat"></div>
<div class="team-card" style="left:482px;top:3080px"><h4>Dr. Elena Ruiz</h4><div class="role">Lorem ipsum</div><p>Lorem ipsum dolor sit amet, consectetur adipiscing elit. Id blandit sed mattis amet scelerisque in risus in.</p></div>

<div class="team-photo" style="left:776px;top:2870px" role="img" aria-label="Portrait of a female doctor with a stethoscope"></div>
<div class="team-card" style="left:809px;top:3080px"><h4>Dr. Clara Novak</h4><div class="role">Lorem ipsum</div><p>Lorem ipsum dolor sit amet, consectetur adipiscing elit. Id blandit sed mattis amet scelerisque in risus in.</p></div>

<div class="nav-circle" style="left:928px;top:3297px;background:#e6e6e8"><svg width="20" height="12" viewBox="0 0 20 12" fill="none" stroke="var(--ink)" stroke-width="1.8"><path d="M20 6H2M7 1L2 6l5 5"/></svg></div>
<div class="nav-circle" style="left:1013px;top:3297px;background:var(--blue)"><svg width="20" height="12" viewBox="0 0 20 12" fill="none" stroke="#fff" stroke-width="1.8"><path d="M0 6h18M13 1l5 5-5 5"/></svg></div>

<!-- Contact -->
<svg class="abs" style="left:0;top:3360px" width="1200" height="620" viewBox="0 0 1200 620">
  <defs>
    <linearGradient id="cb" x1="0" x2="1"><stop offset="0" stop-color="#1a3070"/><stop offset=".6" stop-color="#243d7d"/><stop offset="1" stop-color="#3a4f86"/></linearGradient>
    <linearGradient id="cw" x1="0" x2="1"><stop offset="0" stop-color="#4a3df0"/><stop offset="1" stop-color="#f2507e"/></linearGradient>
  </defs>
  <path d="M0 50C240 10 520 80 820 40S1100 10 1200 20V600H0Z" fill="url(#cb)" role="img" aria-label="Smiling woman in a softly tinted navy background photo"/>
  <path d="M0 574C260 586 560 610 820 590S1100 560 1200 560V620H0Z" fill="url(#cw)"/>
  <path d="M0 590C260 600 560 622 820 606S1100 580 1200 582V620H0Z" fill="#fff"/>
</svg>
<div class="abs eyebrow" style="left:122px;top:3560px;color:#fff">Contact us</div>
<h2 class="abs heading" style="left:122px;top:3584px;font-size:40px;font-weight:400;color:#fff;letter-spacing:1.5px;line-height:44px">LET US ASSIST<br>YOU &amp; YOUR<br>LOVE ONES</h2>
<div class="field" style="left:588px;top:3534px;width:237px;height:40px">Your Name</div>
<div class="field" style="left:838px;top:3534px;width:238px;height:40px">Your Phone</div>
<div class="field" style="left:588px;top:3596px;width:237px;height:40px">Your Email</div>
<div class="field" style="left:838px;top:3596px;width:238px;height:40px">Subject</div>
<div class="field" style="left:588px;top:3658px;width:490px;height:102px;align-items:flex-start;padding-top:20px">How we can help?</div>
<div class="btn" style="left:593px;top:3785px;width:197px;height:52px">Send Message</div>

<!-- Footer -->
<div class="brand" style="left:122px;top:4032px"><span class="brand-dot" style="width:44px;height:44px"></span><span class="brand-name" style="font-size:24px">Wellspring Crest</span></div>
<div class="abs foot-title" style="left:128px;top:4128px">Working Hours</div>
<div class="abs" style="left:128px;top:4163px;width:48px;height:3px;background:var(--grad)"></div>
<div class="abs foot-link" style="left:128px;top:4186px">Mn – Fr : <b style="font-weight:600">8:00 am – 6:30 pm</b></div>
<div class="abs foot-link" style="left:128px;top:4215px">Sat – Su : <b style="font-weight:600">9:00 am – 3:00 pm</b></div>

<div class="abs foot-title" style="left:543px;top:4026px">Quick links</div>
<div class="abs" style="left:543px;top:4060px;width:48px;height:3px;background:var(--grad)"></div>
<div class="abs" style="left:595px;top:4061px;width:190px;height:1px;background:#e2e4ea"></div>
<div class="abs foot-link" style="left:543px;top:4084px">Home</div>
<div class="abs foot-link" style="left:543px;top:4115px">About</div>
<div class="abs foot-link" style="left:543px;top:4146px">Meet The Team</div>
<div class="abs foot-link" style="left:543px;top:4177px">Services</div>
<div class="abs foot-link" style="left:543px;top:4208px">Contact</div>

<div class="abs foot-title" style="left:845px;top:4026px">Contact info</div>
<div class="abs" style="left:845px;top:4060px;width:48px;height:3px;background:var(--grad)"></div>
<div class="abs" style="left:897px;top:4061px;width:180px;height:1px;background:#e2e4ea"></div>
<svg class="abs" style="left:846px;top:4086px" width="14" height="18" viewBox="0 0 14 18" fill="none" stroke="var(--pink)" stroke-width="1.5"><path d="M7 17s6-6 6-10A6 6 0 001 7c0 4 6 10 6 10z"/><circle cx="7" cy="7" r="2"/></svg>
<div class="abs foot-link" style="left:873px;top:4084px;font-size:13.5px;line-height:20px">2210 Harbor Lane,<br>Tampa, Florida 33602</div>
<svg class="abs" style="left:846px;top:4138px" width="16" height="16" viewBox="0 0 16 16" fill="none" stroke="var(--pink)" stroke-width="1.5"><path d="M3 1h3l1.5 4-2 1.3a9 9 0 004.2 4.2L11 8.5l4 1.5v3a2 2 0 01-2 2A12 12 0 011 3a2 2 0 012-2z"/></svg>
<div class="abs foot-link" style="left:873px;top:4137px;font-size:13.5px">(813) 555-0148</div>
<svg class="abs" style="left:846px;top:4176px" width="16" height="12" viewBox="0 0 16 12" fill="none" stroke="var(--pink)" stroke-width="1.5"><rect x="1" y="1" width="14" height="10" rx="1"/><path d="M1 2l7 5 7-5"/></svg>
<div class="abs foot-link" style="left:873px;top:4172px;font-size:13.5px">hello@wellspringcrest.org</div>
<span class="social" style="left:846px;top:4216px"></span>
<span class="social" style="left:888px;top:4216px"></span>
<span class="social" style="left:930px;top:4216px"></span>
<span class="social" style="left:972px;top:4216px"></span>

<div class="abs bottom-bar">
  <span class="abs" style="left:122px;top:9px">©Copyright 2022. <span style="color:#5aa8ff;text-decoration:underline">Wellspring Crest Partners</span> | All Rights Reserved</span>
  <span class="abs" style="left:868px;top:9px">Privacy Policy &nbsp;|&nbsp; Terms and Conditions</span>
</div>

</body>
</html>
```